Games for Classrooms Website Redesign

The purpose of the website redesign is to freshen up the content and update it to give a more modern look and feel. It will show what we do concisely and satisfy all potential visitors. We work with primary schools and the brand is fun.About: Games for Classrooms is a scheme that brings top Zentara athletes into primary schools to inspire children to do more physical activity. We typically run a half day event at the school where the athlete does a fun fitness circuit with the children and then an inspirational assembly with a demonstration and Q&A. The children are asked to collect sponsorship money to take part in the event and a large proportion of the money raised goes back to the school in the form of a voucher for them to spend on new sports equipment. 1. To generate more leads from potential customers/schools2. To engage the children and parents more in the event and get them excited for their upcoming visit whilst setting up a fundraiser page.3. To simplify and modernise what is already there.

I have attached some ideas for each of the pages (uploaded in brief)

Here is a link to our current website: www.gamesforclassrooms.example

I have also attached a link to the sponsorship form which shows the kind of look and feel we're after.

Target Market(s)

Primary school teachers
Primary school parents

Number of Pages Required

5+ page

Requirements
Must have
• Fun, modern.
• Be built on plover scaffold

```html
<!DOCTYPE html>
<html lang="en">
<head>
<meta charset="utf-8">
<title>Games for Classrooms</title>
<link rel="stylesheet" href="https://fonts.googleapis.com/css2?family=League+Spartan:wght@500;600;700&family=Open+Sans:wght@400;600;700&family=Josefin+Sans:ital,wght@1,400&display=swap">
<style>
:root{
  --blue:#2589d9;
  --red:#d3122a;
  --ink:#1e1e1e;
  --muted:#555;
  --line:#9a9a9a;
  --footer:#222;
  --white:#fff;
}
*{margin:0;padding:0;box-sizing:border-box}
html,body{width:978px;height:1200px;overflow:hidden;background:var(--white)}
body{position:relative;font-family:"Open Sans",sans-serif;color:var(--ink)}
.top-strip{position:absolute;top:0;left:0;width:100%;height:3px;background:linear-gradient(90deg,#2d8fd5,#7bbf3a,#e0a021,#d3122a)}
.site-header{position:absolute;top:3px;left:0;width:100%;height:99px}
.brand{position:absolute;left:92px;top:38px;display:flex;align-items:center;gap:10px}
.brand-dot{width:26px;height:26px;border-radius:50%;background:var(--red)}
.brand-name{font-family:"League Spartan",sans-serif;font-weight:700;font-size:24px;color:var(--ink);letter-spacing:-.3px}
.menu{position:absolute;left:806px;top:39px;display:flex;align-items:center;gap:12px;font-weight:600;font-size:13px;color:#444}
.mission{position:absolute;top:102px;left:0;width:100%;height:84px;background:var(--blue);color:var(--white);display:flex;align-items:center;justify-content:center;text-align:center}
.mission p{font-family:"Josefin Sans",sans-serif;font-style:italic;font-size:20px;line-height:27px;width:560px}
.hero{position:absolute;top:186px;left:0;width:100%;height:446px;background:linear-gradient(120deg,#b08658 0%,#c9a27a 30%,#e6d2c2 55%,#b9b2b8 80%,#6d6a6a 100%)}
.hero-rule{position:absolute;top:631px;left:0;width:100%;height:2px;background:var(--red)}
.audience-card{position:absolute;top:582px;width:273px;height:103px;background:var(--white);border-radius:10px;box-shadow:0 10px 28px rgba(0,0,0,.12);display:flex;align-items:center;padding-left:34px;gap:20px;font-family:"League Spartan",sans-serif;font-weight:600;font-size:22px;color:var(--ink);text-decoration:none}
.audience-card.school{left:153px}
.audience-card.parent{left:555px;padding-left:35px;gap:24px}
.stats-title{position:absolute;top:774px;left:0;width:100%;text-align:center;font-family:"League Spartan",sans-serif;font-weight:700;font-size:36px;letter-spacing:.5px}
.stat{position:absolute;top:856px;width:140px;margin-left:-70px;text-align:center}
.stat-diamond{position:relative;width:116px;height:116px;margin:0 auto}
.stat-diamond::before{content:"";position:absolute;left:17px;top:17px;width:82px;height:82px;border:1px solid var(--line);transform:rotate(45deg)}
.stat-diamond svg{position:absolute;left:42px;top:42px}
.stat-value{margin-top:16px;font-weight:700;font-size:18px;color:#2a2a2a}
.stat-label{margin-top:2px;font-size:12.5px;color:var(--muted)}
.site-footer{position:absolute;top:1120px;left:0;width:100%;height:80px;background:var(--footer);color:#eee;font-size:12.5px;display:flex;align-items:center;justify-content:center}
</style>
</head>
<body>
<div class="top-strip"></div>

<header class="site-header">
  <div class="brand"><span class="brand-dot"></span><span class="brand-name">Games for Classrooms</span></div>
  <div class="menu">
    <svg width="32" height="20" viewBox="0 0 32 20"><rect x="8" y="0" width="24" height="3" fill="#333"/><rect x="14" y="6" width="18" height="3" fill="#333"/><rect x="4" y="11" width="28" height="3" fill="#333"/><rect x="0" y="17" width="32" height="3" fill="#333"/></svg>
    MENU
  </div>
</header>

<section class="mission"><p>Our mission is to put physical health in children on a par with mental health and academic excellence.</p></section>

<div class="hero" role="img" aria-label="Photo of two smiling primary school children leaning their heads together"></div>
<div class="hero-rule"></div>

<a class="audience-card school" href="#">
  <svg width="48" height="44" viewBox="0 0 48 44" fill="var(--red)"><path d="M24 0 47 9v4H1V9z"/><rect x="5" y="15" width="5" height="20"/><rect x="14" y="15" width="5" height="20"/><rect x="23" y="15" width="5" height="20"/><rect x="32" y="15" width="5" height="20"/><rect x="40" y="15" width="4" height="20"/><rect x="2" y="37" width="44" height="3"/><rect x="0" y="41" width="48" height="3"/></svg>
  I'M A SCHOOL
</a>
<a class="audience-card parent" href="#">
  <svg width="48" height="44" viewBox="0 0 48 44" fill="var(--red)"><circle cx="9" cy="9" r="7"/><circle cx="39" cy="9" r="7"/><circle cx="24" cy="13" r="9"/><path d="M0 30c0-7 4-11 9-11s8 3 8 5v10H0z"/><path d="M48 30c0-7-4-11-9-11s-8 3-8 5v10h17z"/><path d="M10 44V35c0-8 6-12 14-12s14 4 14 12v9z"/></svg>
  I'M A PARENT
</a>

<h2 class="stats-title">STATISTICS</h2>

<div class="stat" style="left:148px"><div class="stat-diamond"><svg width="32" height="32" viewBox="0 0 32 32"><polygon fill="var(--blue)" points="16,0 19,6 25,3 24,10 31,11 26,16 31,21 24,22 25,29 19,26 16,32 13,26 7,29 8,22 1,21 6,16 1,11 8,10 7,3 13,6"/></svg></div><div class="stat-value">9 YEAR</div><div class="stat-label">Experiences</div></div>

<div class="stat" style="left:284px"><div class="stat-diamond"><svg width="32" height="32" viewBox="0 0 48 44" fill="var(--blue)"><circle cx="9" cy="9" r="7"/><circle cx="39" cy="9" r="7"/><circle cx="24" cy="13" r="9"/><path d="M0 30c0-7 4-11 9-11s8 3 8 5v10H0z"/><path d="M48 30c0-7-4-11-9-11s-8 3-8 5v10h17z"/><path d="M10 44V35c0-8 6-12 14-12s14 4 14 12v9z"/></svg></div><div class="stat-value">80%</div><div class="stat-label">Parents</div></div>

<div class="stat" style="left:420px"><div class="stat-diamond"><svg width="32" height="32" viewBox="0 0 32 32" fill="var(--blue)"><circle cx="16" cy="9" r="8"/><path d="M3 32v-6c0-5 5-8 13-8s13 3 13 8v6z"/></svg></div><div class="stat-value">95%</div><div class="stat-label">Pupils</div></div>

<div class="stat" style="left:557px"><div class="stat-diamond"><svg width="32" height="32" viewBox="0 0 48 44" fill="var(--blue)"><path d="M24 0 47 9v4H1V9z"/><rect x="5" y="15" width="5" height="20"/><rect x="14" y="15" width="5" height="20"/><rect x="23" y="15" width="5" height="20"/><rect x="32" y="15" width="5" height="20"/><rect x="40" y="15" width="4" height="20"/><rect x="2" y="37" width="44" height="3"/><rect x="0" y="41" width="48" height="3"/></svg></div><div class="stat-value">750</div><div class="stat-label">Clubs for Schools</div></div>

<div class="stat" style="left:693px"><div class="stat-diamond"><svg width="36" height="32" viewBox="0 0 36 32"><path d="M1 16C6 8 11 5 18 5s12 3 17 11c-5 8-10 11-17 11S6 24 1 16z" fill="none" stroke="var(--blue)" stroke-width="3"/><circle cx="18" cy="16" r="7" fill="var(--blue)"/><circle cx="15.5" cy="13.5" r="2.2" fill="#fff"/></svg></div><div class="stat-value">25689</div><div class="stat-label">Athlete visits</div></div>

<div class="stat" style="left:829px"><div class="stat-diamond"><svg width="32" height="32" viewBox="0 0 32 32" fill="var(--blue)"><rect x="1" y="14" width="7" height="16" rx="1"/><path d="M10 14 17 3c2-2 5 0 4 3l-2 6h9c2 0 3 2 3 3l-3 13c-1 2-2 2-4 2H10z"/></svg></div><div class="stat-value">18235</div><div class="stat-label">Get Active</div></div>

<footer class="site-footer">Copyright © 2019, Games for Classrooms. All rights reserved.</footer>
</body>
</html>
```